Amber Ridge Dairy Business cards

We need a logo design for our family dairy. Included on the cards should be my name/my husbands name/the dairy name/ all the phone numbers/address and email. The name is Amber Ridge Dairy, LLC. We would like to use our farm mascot pic on the card. We know the pictures I sent you are of a beef cow but she is the mascot of the farm. We were thinking that maybe put a picture of her head in the middle of the card with a "A" on one side and a "D" on the other side with a "R" around the picture of the cow. But we are open to any ideas. We are looking for something kind of professional and a design that that can be used on cards, clothing and a car sign. Black lettering and blue for the other color...or what looks good.

Target Market(s)

All

Industry/Entity Type

Farming

Contact Information for Business Card

Rosa Pelton Owner (555)210-4471
Martin Strube Owner (555)382-9015
Amber Ridge Dairy, LLC (555)647-1238
Amberridgedairy@mailbox.example
7126 County Lane 14, Fernhollow, WI 53999

Font styles to use
Sans Serif

Colors
3176b5
3c7bb8
3277b5
0255a3

Requirements
Must have
• Some design that incorporates a drawing/pic of the cow pictures that were sent.
Nice to have
• no suggestions
Should not have
• no suggestions

```html
<!DOCTYPE html>
<html lang="en">
<head>
<meta charset="utf-8">
<title>Amber Ridge Dairy Business Cards</title>
<link href="https://fonts.googleapis.com/css2?family=Didact+Gothic&family=Crimson+Pro:wght@400&display=swap" rel="stylesheet">
<style>
  :root {
    --page: #ffffff;
    --sky: #3dbfee;
    --card-light: #ffffff;
    --card-dark: #000000;
    --ink: #111111;
    --paper: #ffffff;
    --rule-light: #8a8a8a;
    --rule-dark: #bdbdbd;
    --silver: linear-gradient(90deg, #e4e6e6 0%, #f7f3e2 20%, #dcd8cc 40%, #f1f1ef 60%, #e7e1cc 80%, #dedbc9 100%);
  }
  html, body {
    margin: 0;
    padding: 0;
    width: 978px;
    height: 1200px;
    overflow: hidden;
    background: var(--page);
  }
  .canvas { position: relative; width: 978px; height: 1200px; }
  .band { position: absolute; left: 0; width: 978px; }
  .band--sky { top: 82px; height: 542px; background: var(--sky); }
  .band--silver { top: 658px; height: 542px; background: var(--silver); }
  .card { position: absolute; }
  .card--light { left: 22px; top: 31px; width: 934px; height: 481px; background: var(--card-light); border: 1px solid #9aa; box-sizing: border-box; color: var(--ink); }
  .card--dark { left: 26px; top: 31px; width: 928px; height: 479px; background: var(--card-dark); color: var(--paper); }
  .mark { position: absolute; left: 50%; top: 50px; width: 130px; height: 130px; margin-left: -65px; border-radius: 50%; border: 8px solid currentColor; box-sizing: border-box; }
  .rule { position: absolute; top: 217px; height: 1px; }
  .card--light .rule { left: 325px; width: 284px; background: var(--rule-light); }
  .card--dark .rule { left: 326px; width: 276px; background: var(--rule-dark); }
  .dairy-name { position: absolute; top: 222px; left: 0; width: 100%; text-align: center; font-family: "Didact Gothic", sans-serif; font-size: 20px; letter-spacing: 3px; }
  .contacts { position: absolute; left: 0; top: 0; width: 100%; height: 100%; font-family: "Crimson Pro", serif; font-size: 26px; letter-spacing: -0.6px; }
  .line { position: absolute; white-space: nowrap; line-height: 1; }
  .icon { position: absolute; width: 24px; height: 24px; }
  .card--light .icon { fill: var(--ink); }
  .card--dark .icon { fill: var(--paper); }
</style>
</head>
<body>
<div class="canvas">

  <section class="band band--sky">
    <article class="card card--light">
      <div class="mark" aria-hidden="true"></div>
      <div class="rule"></div>
      <div class="dairy-name">Amber Ridge Dairy</div>
      <div class="contacts">
        <svg class="icon" style="left:163px;top:318px" viewBox="0 0 24 24" aria-label="phone">
          <rect width="24" height="24" rx="2"/>
          <path d="M9 5c-2 1-3 3-3 7s1 6 3 7l2-1-1-3-1 0c-.5-1-.5-5 0-6l1 0 1-3z" fill="#fff"/>
        </svg>
        <span class="line" style="left:200px;top:298px">Rosa Pelton (555)210-4471 / Martin Strube (555)382-9015</span>
        <span class="line" style="left:204px;top:332px">Amber Ridge Dairy, LLC (555)647-1238</span>
        <svg class="icon" style="left:163px;top:377px" viewBox="0 0 24 24" aria-label="email">
          <rect width="24" height="24" rx="2"/>
        </svg>
        <span class="line" style="left:202px;top:374px">Amberridgedairy@mailbox.example</span>
        <span class="line" style="left:204px;top:412px">7126 County Lane 14, Fernhollow, WI 53999</span>
      </div>
    </article>
  </section>

  <section class="band band--silver">
    <article class="card card--dark">
      <div class="mark" aria-hidden="true"></div>
      <div class="rule"></div>
      <div class="dairy-name">Amber Ridge Dairy</div>
      <div class="contacts">
        <svg class="icon" style="left:160px;top:318px" viewBox="0 0 24 24" aria-label="phone">
          <rect width="24" height="24" rx="2"/>
          <path d="M9 5c-2 1-3 3-3 7s1 6 3 7l2-1-1-3-1 0c-.5-1-.5-5 0-6l1 0 1-3z" fill="#000"/>
        </svg>
        <span class="line" style="left:196px;top:298px">Rosa Pelton (555)210-4471 / Martin Strube (555)382-9015</span>
        <span class="line" style="left:200px;top:332px">Amber Ridge Dairy, LLC (555)647-1238</span>
        <svg class="icon" style="left:160px;top:377px" viewBox="0 0 24 24" aria-label="email">
          <rect width="24" height="24" rx="2"/>
        </svg>
        <span class="line" style="left:198px;top:374px">Amberridgedairy@mailbox.example</span>
        <span class="line" style="left:200px;top:412px">7126 County Lane 14, Fernhollow, WI 53999</span>
      </div>
    </article>
  </section>

</div>
</body>
</html>
```